Corporate consulting business needs a business card

I want a professional business card.... surprise me

Updates

Reason: i dont think 2 days is enough

Target Market(s)

Corprorate and Not for Profit firms and organisations

Industry/Entity Type

Consulting

Contact Information for Business Card

Logo
Corporate Consulting Services
On Time, On Budget, Beyond Expectation
Tovan Presfield
Director
0427 31 94 62 (Larger)
tovan@tp-advisory.com.au
www.tp-advisory.com.au
include little icons beside the contact info:

- Envelope = email
- Phone = phone
- Globe = website

Font styles to use
Serif
Sans Serif

Requirements
Must have
• Professional and clean
Nice to have
• you tell me

```html
<!DOCTYPE html>
<html lang="en">
<head>
<meta charset="utf-8">
<title>Presfield Consulting Services – Business Card</title>
<link rel="stylesheet" href="https://fonts.googleapis.com/css2?family=Cinzel:wght@600;700&family=Montserrat:wght@300;400;600;700&display=swap">
<style>
  :root {
    --backdrop: #ece9e5;
    --card: #ffffff;
    --brown: #6b3f22;
    --brown-soft: #8a5a3c;
    --ink: #3a3533;
    --grey-light: #8d8a88;
    --faint: #e4e1dd;
    --block: #e7e5e2;
    --taupe: #9c8f84;
    --serif: "Cinzel", Georgia, serif;
    --sans: "Montserrat", Arial, sans-serif;
  }
  * { box-sizing: border-box; margin: 0; padding: 0; }
  html, body { width: 1200px; height: 800px; overflow: hidden; }
  body { background: var(--backdrop); position: relative; font-family: var(--sans); }

  .card {
    position: absolute; top: 245px; width: 540px; height: 310px;
    background: var(--card); overflow: hidden;
    box-shadow: 0 6px 18px rgba(0,0,0,.12);
  }
  .card--front { left: 40px; }
  .card--back { left: 620px; }

  .faint-ring { position: absolute; border-radius: 50%; border: 5px solid var(--faint); }

  /* Front */
  .card--front .faint-ring { left: 345px; top: 40px; width: 270px; height: 270px; }
  .brand { position: absolute; display: flex; align-items: center; gap: 14px; }
  .brand__ring { border-radius: 50%; border: 4px solid var(--brown); flex: none; }
  .brand__name { font-family: var(--serif); font-weight: 700; color: var(--brown); }
  .card--front .brand { left: 130px; top: 62px; }
  .card--front .brand__ring { width: 84px; height: 84px; }
  .card--front .brand__name { font-size: 34px; }
  .services { position: absolute; font-family: var(--serif); font-weight: 700; color: var(--ink); letter-spacing: .5px; }
  .card--front .services { left: 0; width: 100%; text-align: center; top: 178px; font-size: 25px; padding-right: 40px; }
  .base-band { position: absolute; left: 0; bottom: 0; width: 100%; height: 24px; background: var(--taupe); }

  /* Back */
  .card--back .faint-ring { left: 110px; top: 95px; width: 190px; height: 190px; }
  .grey-block { position: absolute; left: 270px; top: 0; width: 52px; height: 78px; background: var(--block); }
  .holder { position: absolute; left: 300px; top: 62px; }
  .holder__name { font-size: 19px; letter-spacing: .5px; text-transform: uppercase; color: var(--grey-light); font-weight: 300; }
  .holder__name strong { color: var(--ink); font-weight: 700; }
  .holder__role { font-size: 11px; letter-spacing: 1.5px; color: var(--brown-soft); text-transform: uppercase; margin-top: 1px; }
  .brown-band { position: absolute; left: 280px; top: 130px; width: 32px; height: 180px; background: var(--brown); }
  .icon { position: absolute; left: 286px; width: 20px; height: 20px; }
  .contact { position: absolute; left: 326px; color: var(--ink); }
  .contact--phone { top: 150px; font-size: 15px; font-weight: 600; letter-spacing: .5px; }
  .contact--mail { top: 198px; font-size: 12px; }
  .contact--web { top: 216px; font-size: 12px; }
  .card--back .brand { left: 30px; top: 150px; gap: 10px; }
  .card--back .brand__ring { width: 54px; height: 54px; border-width: 3px; }
  .card--back .brand__name { font-size: 22px; }
  .card--back .services { left: 30px; top: 216px; font-size: 14px; }
</style>
</head>
<body>

<section class="card card--front" aria-label="Card front">
  <div class="faint-ring"></div>
  <div class="brand">
    <span class="brand__ring"></span>
    <span class="brand__name">Presfield</span>
  </div>
  <p class="services">Consulting Services</p>
  <div class="base-band"></div>
</section>

<section class="card card--back" aria-label="Card back">
  <div class="faint-ring"></div>
  <div class="grey-block"></div>
  <div class="holder">
    <p class="holder__name"><strong>Tovan</strong> Presfield</p>
    <p class="holder__role">Director</p>
  </div>
  <div class="brand">
    <span class="brand__ring"></span>
    <span class="brand__name">Presfield</span>
  </div>
  <p class="services">Consulting Services</p>

  <div class="brown-band"></div>
  <svg class="icon" style="top:149px" viewBox="0 0 20 20" aria-label="Phone">
    <circle cx="10" cy="10" r="10" fill="#fff"/>
    <path d="M6.5 5h2l1 2.6-1.3 1c.6 1.3 1.6 2.3 2.9 2.9l1-1.3 2.6 1v2c0 .6-.5 1-1 1C9 14 6 11 5.5 6c0-.5.4-1 1-1z" fill="#6b3f22"/>
  </svg>
  <svg class="icon" style="top:198px" viewBox="0 0 20 20" aria-label="Email">
    <circle cx="10" cy="10" r="10" fill="#fff"/>
    <rect x="5" y="6.5" width="10" height="7" rx="1" fill="#6b3f22"/>
    <path d="M5.5 7l4.5 3.5L14.5 7" stroke="#fff" stroke-width="1" fill="none"/>
  </svg>
  <p class="contact contact--phone">0427 31 94 62</p>
  <p class="contact contact--mail">tovan@tp-advisory.com.au</p>
  <p class="contact contact--web">www.tp-advisory.com.au</p>
</section>

</body>
</html>
```